Pharmacy ad

need 2 pharmacy ads for the phone book. one for Birchfield Pharmacy and one for Corvane Rx Pharmacy. Dimensions for ad is 4.75in x 4.667 in. please see attached examples of ad uploaded as well logos of each pharmacy

```html
<!DOCTYPE html>
<html lang="en">
<head>
<meta charset="utf-8">
<title>Corvane Rx Pharmacy – Directory Ad</title>
<link rel="stylesheet" href="https://fonts.googleapis.com/css2?family=PT+Sans:wght@400;700&family=PT+Sans+Narrow:wght@400;700&family=Montserrat:wght@600&display=swap">
<style>
  :root {
    --brand-blue: #3b51a3;
    --deep-navy: #2a3370;
    --footer-navy: #262c5c;
    --promo-red: #ec1c24;
    --promo-yellow: #ffe600;
    --leaf-green: #7cc242;
    --white: #ffffff;
    --coat-white: #f3f4f4;
    --coat-shade: #dfe3e6;
    --shelf-blue: #8fa6c4;
    --shelf-teal: #9cc3c8;
    --shelf-red: #d9a3a0;
    --skin-warm: #d9b8a6;
    --hair-dark: #6b5044;
  }
  html, body {
    margin: 0;
    padding: 0;
    overflow: hidden;
    background: var(--white);
  }
  .ad {
    position: relative;
    width: 1200px;
    height: 1179px;
    overflow: hidden;
    background: var(--brand-blue);
    font-family: "PT Sans", sans-serif;
    color: var(--white);
  }
  .hero-photo {
    position: absolute;
    left: 0; top: 0;
    width: 1200px; height: 895px;
    background:
      radial-gradient(ellipse 150px 320px at 1150px 300px, rgba(107,80,68,0.75) 0%, rgba(107,80,68,0) 75%),
      radial-gradient(ellipse 230px 190px at 960px 250px, rgba(217,184,166,0.95) 0%, rgba(217,184,166,0) 75%),
      radial-gradient(ellipse 180px 60px at 1030px 790px, rgba(232,205,190,0.9) 0%, rgba(232,205,190,0) 80%),
      radial-gradient(ellipse 420px 380px at 880px 600px, var(--coat-white) 0%, rgba(243,244,244,0.6) 60%, rgba(243,244,244,0) 100%),
      radial-gradient(ellipse 180px 260px at 420px 580px, rgba(143,166,196,0.7) 0%, rgba(143,166,196,0) 80%),
      radial-gradient(ellipse 160px 200px at 120px 680px, rgba(217,163,160,0.75) 0%, rgba(217,163,160,0) 80%),
      radial-gradient(ellipse 200px 160px at 260px 520px, rgba(156,195,200,0.7) 0%, rgba(156,195,200,0) 80%),
      radial-gradient(ellipse 140px 180px at 560px 720px, rgba(217,163,160,0.5) 0%, rgba(217,163,160,0) 80%),
      linear-gradient(180deg, #e6ebef 0%, var(--coat-shade) 55%, #d3d9de 100%);
  }
  .top-wave {
    position: absolute;
    left: 0; top: 0;
    width: 1200px; height: 470px;
  }
  .brand {
    position: absolute;
    right: 30px; top: 62px;
    display: flex;
    align-items: center;
    gap: 26px;
  }
  .brand-mark {
    width: 56px; height: 56px;
    border-radius: 50%;
    background: var(--leaf-green);
  }
  .brand-name {
    font-family: "Montserrat", sans-serif;
    font-weight: 600;
    color: var(--white);
    line-height: 1;
  }
  .brand-name .primary { display: block; font-size: 68px; letter-spacing: -1px; }
  .brand-name .secondary { display: block; font-size: 36px; letter-spacing: 2px; margin-top: 6px; text-align: center; }
  .services {
    position: absolute;
    left: 33px; top: 118px;
    margin: 0; padding: 0;
    list-style: none;
    font-weight: 700;
    font-size: 32px;
    line-height: 42px;
  }
  .info-band {
    position: absolute;
    left: 0; top: 895px;
    width: 1200px; height: 158px;
    background: var(--brand-blue);
  }
  .promo {
    position: absolute;
    top: 822px;
    width: 348px; height: 152px;
    border-radius: 30px;
    background: var(--promo-red);
    text-align: center;
    box-sizing: border-box;
  }
  .promo-senior { left: 29px; }
  .promo-student { left: 427px; }
  .promo-hours { left: 825px; }
  .promo .rate {
    display: block;
    color: var(--promo-yellow);
    font-weight: 700;
    font-size: 56px;
    line-height: 1;
    padding-top: 12px;
  }
  .promo .label {
    display: block;
    font-weight: 700;
    font-size: 30px;
    line-height: 1.1;
    margin-top: 4px;
  }
  .promo .note {
    display: block;
    font-size: 19px;
    margin-top: 4px;
  }
  .promo-hours {
    font-family: "PT Sans Narrow", sans-serif;
    font-weight: 700;
    font-size: 33px;
    line-height: 41px;
    padding-top: 14px;
  }
  .contact-line {
    position: absolute;
    left: 0; top: 986px;
    width: 1200px;
    margin: 0;
    text-align: center;
    font-family: "PT Sans Narrow", sans-serif;
    font-size: 27px;
  }
  .payments {
    position: absolute;
    left: 0; top: 1053px;
    width: 1200px; height: 117px;
    background: var(--white);
  }
  .accept-tab {
    position: absolute;
    left: 526px; top: 1029px;
    width: 150px; height: 42px;
    background: var(--deep-navy);
    font-weight: 700;
    font-size: 21px;
    line-height: 42px;
    text-align: center;
  }
  .partner {
    position: absolute;
    top: 1091px;
    display: flex;
    align-items: center;
    gap: 10px;
    transform: translateX(-50%);
    font-weight: 700;
    font-size: 30px;
    color: var(--deep-navy);
    white-space: nowrap;
  }
  .partner .dot {
    width: 20px; height: 20px;
    background: var(--deep-navy);
  }
  .partner-card { left: 135px; }
  .partner-life { left: 345px; }
  .partner-pay { left: 570px; }
  .partner-insure { left: 935px; }
  .footer-bar {
    position: absolute;
    left: 0; top: 1170px;
    width: 1200px; height: 9px;
    background: var(--footer-navy);
  }
</style>
</head>
<body>
<main class="ad">
  <div class="hero-photo" role="img" aria-label="Smiling pharmacist in a white coat at the counter, with blurred pharmacy shelves behind"></div>

  <svg class="top-wave" viewBox="0 0 1200 470" aria-hidden="true">
    <path fill="#3b51a3" d="M0 0 H1200 V193 C1000 188 880 200 760 252 C620 330 520 452 300 457 C180 460 60 442 0 464 Z"/>
  </svg>

  <div class="brand">
    <span class="brand-mark" aria-hidden="true"></span>
    <span class="brand-name">
      <span class="primary">Corvane Rx</span>
      <span class="secondary">PHARMACY</span>
    </span>
  </div>

  <ul class="services">
    <li>Certified Pharmacists</li>
    <li>Affordable prices</li>
    <li>Brand and Generic Medicines</li>
    <li>Blood Pressure and Glucose checks</li>
    <li>Personal care and Beauty Products</li>
    <li>Injectables Special Orders</li>
    <li>Delivery service</li>
  </ul>

  <div class="info-band"></div>

  <div class="promo promo-senior">
    <span class="rate">10%</span>
    <span class="label">senior citizen discount</span>
    <span class="note">For patients 60 years and over</span>
  </div>
  <div class="promo promo-student">
    <span class="rate">10%</span>
    <span class="label">Student discount</span>
    <span class="note">With valid ID card</span>
  </div>
  <div class="promo promo-hours">
    Monday – Saturday,<br>
    Thursday 8am- 7pm<br>
    Sunday 10am-2pm
  </div>

  <p class="contact-line">Unit B4, Queens Harbour Hotel, Shore Road, Port Ellery | Phone: 472-3108 (Visit us on Chatterly)</p>

  <div class="payments"></div>
  <div class="accept-tab">We accept</div>
  <div class="partner partner-card"><span class="dot"></span>Meridian Card</div>
  <div class="partner partner-life"><span class="dot"></span>Sollance</div>
  <div class="partner partner-pay"><span class="dot"></span>Vantra</div>
  <div class="partner partner-insure"><span class="dot"></span>Harbourline Insurances</div>

  <div class="footer-bar"></div>
</main>
</body>
</html>
```